Business Card Design Project

I would like to have a project of business card with incorporated attachted logo elements in warm colors like: gold, yellow, brown.
We would like incorporate below information into the design
Name of the Company: Continental Hoop Invitational
Name: Dorian Pelkey
Position: Project Director
e-mail: dorian@hoopinvitational.net
mobile: +65 83147092
website: www.hoopinvitational.net
Address: 47 Marbury Lane, #06-11, Singapore 915274
There is a picture attachted which can be used as a back side of the buisness card - we would like to follow the colors theme on the front card ( with the person contact details) how ever the front card we will prefer with white background but with graphfic elements coming from logo.
Project Deadline Extended
Reason: the project has been launched on 24 of April with deadline by 24 of April by mistakes. Thats why I would like to extend the deadline.
Name: Dorian Pelkey
mobile: +65 83147092

```html
<!DOCTYPE html>
<html lang="en">
<head>
<meta charset="utf-8">
<title>Dorian Pelkey – Business Card</title>
<link href="https://fonts.googleapis.com/css2?family=Montserrat:wght@400;500;700&display=swap" rel="stylesheet">
<style>
  :root {
    --stage: #d9d9d9;
    --gold-light: #f0df3a;
    --gold-mid: #d2b416;
    --ochre: #bb7f22;
    --bronze: #8a5a12;
    --yellow: #e6d600;
    --ink: #141008;
    --ink-soft: #2b2108;
    --night: #050505;
  }
  html, body {
    margin: 0;
    width: 1200px;
    height: 900px;
    overflow: hidden;
    background: var(--stage);
    font-family: "Montserrat", sans-serif;
  }
  .canvas { position: relative; width: 1200px; height: 900px; }
  .card {
    position: absolute;
    width: 614px;
    height: 338px;
    border-radius: 14px;
    overflow: hidden;
  }
  .card-front {
    left: 104px; top: 72px;
    background:
      radial-gradient(circle at 160px 90px, var(--gold-light) 0, var(--gold-mid) 150px, transparent 330px),
      linear-gradient(90deg, var(--gold-mid) 0%, var(--ochre) 70%, #b57522 100%);
  }
  .card-back { left: 484px; top: 482px; background: var(--night); }
  .wave { position: absolute; left: 0; top: 0; width: 614px; height: 338px; }
  .holder-name {
    position: absolute; left: 27px; top: 112px; margin: 0;
    font-size: 30px; letter-spacing: -0.5px; color: var(--ink);
    font-weight: 400; line-height: 1;
    padding-bottom: 4px; border-bottom: 1px solid rgba(20,16,8,0.45);
  }
  .holder-name strong { font-weight: 700; }
  .holder-role {
    position: absolute; left: 31px; top: 151px; margin: 0;
    font-size: 12px; font-weight: 500; color: var(--ink-soft);
  }
  .divider {
    position: absolute; left: 301px; top: 54px; width: 1px; height: 194px;
    background: var(--ink-soft);
  }
  .contact-list {
    position: absolute; left: 327px; top: 126px; margin: 0; padding: 0;
    list-style: none; font-size: 11px; color: var(--ink-soft);
  }
  .contact-list li { display: flex; align-items: center; height: 19.5px; }
  .contact-icon {
    width: 10px; height: 10px; border-radius: 50%;
    background: var(--bronze); margin-right: 8px; flex: none;
  }
  .emblem {
    position: absolute; left: 222px; top: 40px; width: 170px; height: 180px;
    border-radius: 50%;
    background: radial-gradient(circle at 50% 50%, #8d5a1a 0, #5a3410 45%, rgba(5,5,5,0) 72%);
  }
</style>
</head>
<body>
<div class="canvas">
  <section class="card card-front" aria-label="Business card front">
    <svg class="wave" viewBox="0 0 614 338" aria-hidden="true">
      <defs>
        <linearGradient id="frontBase" x1="0" x2="1" y1="0" y2="0">
          <stop offset="0" stop-color="#c39a12"/>
          <stop offset="0.6" stop-color="#d2b10e"/>
          <stop offset="1" stop-color="#e6d600"/>
        </linearGradient>
      </defs>
      <path d="M0 172 C40 250 140 300 260 296 C340 292 420 280 470 288 C530 298 580 320 614 338 L0 338 Z" fill="#9a6614"/>
      <path d="M0 190 C50 262 150 310 260 306 C340 302 420 288 470 296 C530 306 580 326 614 340 L0 340 Z" fill="url(#frontBase)"/>
    </svg>
    <h1 class="holder-name"><strong>Dorian</strong>Pelkey</h1>
    <p class="holder-role">Project Director</p>
    <div class="divider"></div>
    <ul class="contact-list">
      <li><span class="contact-icon"></span>+65 83147092</li>
      <li><span class="contact-icon"></span>dorian@hoopinvitational.net</li>
      <li><span class="contact-icon"></span>www.hoopinvitational.net</li>
      <li><span class="contact-icon"></span>47 Marbury Lane, #06-11, Singapore 915274</li>
    </ul>
  </section>

  <section class="card card-back" aria-label="Business card back">
    <div class="emblem" role="img" aria-label="Event emblem: performer on a vertical pole in front of a bronze crest"></div>
    <svg class="wave" viewBox="0 0 614 338" aria-hidden="true">
      <defs>
        <linearGradient id="backBase" x1="0" x2="1" y1="0" y2="0">
          <stop offset="0" stop-color="#e6d600"/>
          <stop offset="0.5" stop-color="#d4b40c"/>
          <stop offset="1" stop-color="#b98a12"/>
        </linearGradient>
      </defs>
      <path d="M0 332 C80 300 170 286 260 284 C360 284 420 292 480 262 C540 232 585 185 614 140 L614 338 L0 338 Z" fill="#8a5a12"/>
      <path d="M0 338 C80 308 170 294 260 292 C360 292 430 302 490 274 C545 248 590 205 614 168 L614 338 Z" fill="url(#backBase)"/>
    </svg>
  </section>
</div>
</body>
</html>
```